Gourmet butcher shop needs a business card design

We need a business card design for an upmarket butcher shop in Brisbane, Queensland Australia. We would prefer the card to be printed on a brown craft paper business card and would consider the use of raised print on the card. The card needs to make space for the usual information: ABN, address, telephone, facebook page. I stress it is a gourmet shop in a wealthy suburb. Thanks

Industry/Entity Type

Business

Contact Information for Business Card

Address Shop 2, Marrowbank Arcade, 417 Hollister Road, Kelwyn Park
Telephone 07 3581 4927
A.B.N. 53 874 910 326
Facebook www.facebook.com/quillbyprimecuts

Requirements
Should not have
• No need for a person's name or title

```html
<!DOCTYPE html>
<html lang="en">
<head>
<meta charset="utf-8">
<title>Quillby Prime Cuts – Business Card</title>
<link rel="stylesheet" href="https://fonts.googleapis.com/css2?family=Libre+Baskerville:ital,wght@0,400;0,700;1,400&display=swap">
<style>
  :root {
    --backdrop: #2a2c2e;
    --kraft: #c79b5c;
    --kraft-light: #cfa565;
    --ink: #7d5527;
    --ink-soft: #94683a;
  }
  * { box-sizing: border-box; margin: 0; padding: 0; }
  html, body {
    width: 1000px;
    height: 1200px;
    overflow: hidden;
    background: var(--backdrop);
    font-family: "Libre Baskerville", Georgia, serif;
    color: var(--ink);
  }
  .stage {
    width: 1000px;
    height: 1200px;
    display: grid;
    grid-template-rows: 600px 600px;
    place-items: center;
  }
  .card {
    position: relative;
    width: 660px;
    height: 380px;
    overflow: hidden;
    background: radial-gradient(ellipse at 40% 30%, var(--kraft-light), var(--kraft) 70%);
    box-shadow: 0 12px 30px rgba(0,0,0,0.45);
  }

  /* ---------- front ---------- */
  .card-front {
    display: flex;
    flex-direction: column;
    align-items: center;
    justify-content: space-between;
    padding: 36px 30px 40px;
  }
  .rule {
    width: 100%;
    display: flex;
    align-items: center;
    gap: 10px;
  }
  .rule-line { flex: 1; height: 2px; background: var(--ink-soft); }
  .rule-dashes {
    width: 34px;
    height: 2px;
    background: repeating-linear-gradient(90deg, var(--ink-soft) 0 9px, transparent 9px 14px);
  }
  .tagline {
    font-style: italic;
    font-size: 21px;
    color: var(--ink);
    padding: 0 10px;
    white-space: nowrap;
  }
  .brand-name {
    text-align: center;
    font-weight: 700;
    text-transform: uppercase;
    color: var(--ink);
    line-height: 1;
  }
  .brand-name .line-upper {
    display: block;
    font-size: 44px;
    letter-spacing: 4px;
  }
  .brand-name .line-main {
    display: block;
    font-size: 160px;
    letter-spacing: 8px;
    margin-top: 2px;
  }

  /* ---------- back ---------- */
  .card-back {
    display: flex;
    align-items: center;
    justify-content: center;
  }
  .frame {
    position: absolute;
    inset: 24px;
    border: 2px solid var(--ink-soft);
  }
  .frame-dash {
    position: absolute;
    width: 18px;
    height: 2px;
    background: repeating-linear-gradient(90deg, var(--ink-soft) 0 7px, transparent 7px 11px);
  }
  .frame-dash.tl { top: 24px; left: 4px; }
  .frame-dash.tr { top: 24px; right: 4px; }
  .frame-dash.bl { bottom: 24px; left: 4px; }
  .frame-dash.br { bottom: 24px; right: 4px; }
  .contact {
    position: relative;
    text-align: center;
    line-height: 1.05;
  }
  .contact dt {
    font-size: 12px;
    font-weight: 700;
    letter-spacing: 1.5px;
    text-transform: uppercase;
    margin-top: 8px;
  }
  .contact dt:first-child { margin-top: 0; }
  .contact dd {
    font-size: 32px;
    white-space: nowrap;
  }
</style>
</head>
<body>
<main class="stage">
  <section class="card card-front" aria-label="Business card front">
    <div class="rule rule-top">
      <span class="rule-dashes"></span>
      <span class="rule-line"></span>
      <span class="tagline">Always cut finer</span>
      <span class="rule-line"></span>
      <span class="rule-dashes"></span>
    </div>
    <h1 class="brand-name">
      <span class="line-upper">Quillby Prime</span>
      <span class="line-main">Cuts</span>
    </h1>
    <div class="rule rule-bottom">
      <span class="rule-dashes"></span>
      <span class="rule-line"></span>
      <span class="rule-dashes"></span>
    </div>
  </section>

  <section class="card card-back" aria-label="Business card back">
    <div class="frame"></div>
    <span class="frame-dash tl"></span>
    <span class="frame-dash tr"></span>
    <span class="frame-dash bl"></span>
    <span class="frame-dash br"></span>
    <dl class="contact">
      <dt>Phone</dt>
      <dd>07 3581 4927</dd>
      <dt>Address</dt>
      <dd>417 Hollister Road, Kelwyn Park</dd>
      <dt>Facebook</dt>
      <dd>quillbyprimecuts</dd>
      <dt>A.B.N.</dt>
      <dd>53 874 910 326</dd>
    </dl>
  </section>
</main>
</body>
</html>
```